UK Based Internet hosting Company wants a vibrant eCommerce site designed.

We have only just had our logo and brand designed by Pixel Forum which went so well that we would like to open up our website design project on here too.

The company is called 'Quay Server Lantern' and we provide a range of website hosting, dedicated server, domain name and email solutions that people will be able to purchase online in neatly packaged options from the outset.

Our logo and brand is bright turquoise, black & white (samples of branding will be attached with this project) but we would like the website to be very vibrant with good use of white space rather than a black website.

We want to appeal to end users so web designers, developers and people who would like to host their website. But we also want to appeal to resellers that would like to resell our hosting packages too.

We want a big push on social media and blogging on the site as we would like our brand to be 100% up with Chatterleaf, Murmel, workLoop, Vidplume and Zorbix+. It would be great to have this integrated into the site with share buttons and rating buttons etc.

We would like to see a homepage initially with a view to providing several page layers down to help our in-house developers hook in our back-end into this front end effectively.

Great customer experience and an easy to navigate journey to the checkout when purchasing the hosting packages is paramount !!

We like how the following sites are set-out and presented:

www.brightmarrow.uk
http://www.tallyfold.co.uk
https://www.qv7.net/web-hosting/

Target Market(s)

We have 3 target markets.

Target market 1 - end users, consumers such as Web Designers, Developers and small businesses.

Target Market 2 - Resellers, small businesses that would like to resell our services.

Target Market 3 - Medium to large businesses that would like more of a bespoke solution.

Industry/Entity Type

Internet

Requirements
Must have
• Colourful, bright, bold, easy to navigate and to purchase packages.
• Plenty of call to actions, social media, ratings.
• Video case studies and testimonials would be nice.

```html
<!DOCTYPE html>
<html lang="en">
<head>
<meta charset="utf-8">
<title>Quay Server Lantern – Super-fast Webhosting</title>
<link rel="stylesheet" href="https://fonts.googleapis.com/css2?family=Dosis:wght@300;400;500;700&family=PT+Sans:ital,wght@0,400;0,700;1,400&display=swap">
<style>
:root{
  --teal:#1fb8b8;
  --teal-light:#6fcc9f;
  --teal-dark:#13a9b4;
  --ink:#222;
  --text:#444;
  --muted:#8a8a8a;
  --hero-bg:#f4f4f4;
  --card-top:#fbfbfb;
  --card-bottom:#dedede;
  --btn:#111;
  --panel:#ece8ea;
}
*{box-sizing:border-box;margin:0;padding:0}
html,body{width:1002px;height:1200px;overflow:hidden;background:#fff}
body{position:relative;font-family:"PT Sans",sans-serif;color:var(--text)}
.abs{position:absolute}
.top-rule{left:0;top:0;width:1002px;height:3px;background:var(--teal-light)}
.account-tab{left:790px;top:3px;width:130px;height:29px;background:linear-gradient(var(--teal-light),var(--teal));border-radius:0 0 3px 3px;color:#fff;font-size:10px;display:flex;align-items:center;justify-content:center;gap:12px;text-transform:uppercase}
.brand{left:82px;top:26px;display:flex;align-items:center;gap:8px}
.brand-dot{width:36px;height:36px;border-radius:50%;background:var(--teal)}
.brand-name{font-family:"Dosis",sans-serif;font-weight:500;font-size:17px;color:#333;line-height:1}
.main-nav{left:82px;top:94px;width:838px;height:43px;background:linear-gradient(var(--teal-light),var(--teal));border-radius:2px;display:flex}
.main-nav a{color:#fff;text-decoration:none;font-family:"Dosis",sans-serif;font-size:13.5px;letter-spacing:.3px;text-transform:uppercase;display:flex;align-items:center;padding:0 24px;border-right:1px solid rgba(255,255,255,.35)}
.main-nav a:last-child{border-right:none}
.hero{left:0;top:137px;width:1002px;height:509px;background:linear-gradient(#fff,var(--hero-bg) 40%,#efefef);border-bottom:1px solid #5cc3c6}
.hero-kicker{left:82px;top:186px;font-family:"Dosis",sans-serif;font-weight:300;font-size:33px;line-height:40px;color:#111}
.hero-title{left:80px;top:226px;font-family:"Dosis",sans-serif;font-weight:700;font-size:76px;line-height:80px;color:var(--teal);text-shadow:0 3px 0 #bbb}
.hero-sub{left:82px;top:324px;font-size:17px;line-height:21px;color:#444;width:430px}
.hero-dots{left:82px;top:384px;display:flex;gap:8px}
.hero-dots span{width:12px;height:12px;border-radius:50%;background:#ddd}
.hero-dots span:first-child{background:var(--teal)}
.hero-art{left:510px;top:154px;width:328px;height:271px;background:linear-gradient(90deg,#3a3a3a,#8c8c8c 40%,#d0d0d0 60%,#2a2a2a);opacity:.85}
.feature-band{left:82px;top:425px;width:838px;height:193px;background:linear-gradient(var(--teal-light),var(--teal));border-radius:2px}
.card{top:439px;width:249px;height:161px;background:linear-gradient(var(--card-top),var(--card-bottom));border-radius:2px;box-shadow:0 2px 4px rgba(0,0,0,.2)}
.card-head{height:55px;border-bottom:1px solid #ddd;background:linear-gradient(#fff,#ececec);padding:10px 14px;font-family:"Dosis",sans-serif;font-size:25px;color:var(--teal-dark);position:relative}
.card-icon{position:absolute;right:14px;top:-8px;width:48px;height:52px;border-radius:50%;background:radial-gradient(circle at 35% 35%,#bfe4f7,#3a8fc9)}
.card-icon.drive{border-radius:6px;background:linear-gradient(#e8e8e8,#9a9a9a)}
.card-icon.tower{border-radius:4px;width:32px;right:20px;background:linear-gradient(90deg,#888,#eee,#888)}
.card p{font-size:10px;line-height:12px;color:#222;padding:13px 14px 0}
.btn{display:inline-block;background:linear-gradient(#333,#000);color:#fff;font-size:10px;border-radius:3px;height:32px;line-height:32px;padding:0 14px;text-decoration:none}
.card .btn{position:absolute;left:14px;top:113px}
.search{position:absolute;left:14px;top:66px;width:221px;height:35px;background:#fff;border:1px solid #d6d6d6}
.welcome{left:0;top:646px;width:1002px;height:351px;background:linear-gradient(#fff,#e9f8f8);border-bottom:2px solid var(--teal)}
.welcome h2{position:absolute;left:82px;top:32px;font-weight:400;font-size:27px;color:#333}
.welcome h2 span{color:var(--teal)}
.video-frame{left:82px;top:742px;width:263px;height:200px;background:#fff;box-shadow:0 1px 4px rgba(0,0,0,.25);padding:7px}
.video-still{width:249px;height:186px;background:linear-gradient(160deg,#e8eef2,#6e7a84 45%,#20262b 70%,#dfe5e8);position:relative}
.play{position:absolute;left:72px;top:72px;width:55px;height:50px;background:rgba(30,30,30,.7);border-radius:3px}
.play::after{content:"";position:absolute;left:22px;top:14px;border-left:18px solid #fff;border-top:11px solid transparent;border-bottom:11px solid transparent}
.welcome-copy{left:365px;top:740px;width:318px;font-size:11px;line-height:17px;color:#333}
.welcome-copy p+p{margin-top:17px}
.welcome-btn{left:365px;top:902px;height:37px;line-height:37px}
.testimonials{left:700px;top:646px;width:220px;height:349px;background:linear-gradient(#fbf8f9,var(--panel));padding:0 17px}
.testimonials h3{margin-top:34px;font-family:"Dosis",sans-serif;font-weight:400;font-size:26px;color:var(--teal);display:flex;justify-content:space-between;align-items:center}
.testimonials h3 small{font-size:22px;color:#333;letter-spacing:2px}
.quote{margin-top:16px;font-size:11px;line-height:17px;color:var(--muted)}
.quote-mark{font-family:Georgia,serif;font-size:60px;color:#ccc;line-height:30px;float:left;margin:4px 6px 0 0}
.quote p+p{margin-top:17px}
.stars{margin-top:10px;color:#9a9a9a;font-size:11px;letter-spacing:1px}
.author{margin-top:45px;font-style:italic;font-size:12px;color:#444}
.footer-col h4{font-family:"Dosis",sans-serif;font-weight:400;font-size:26px;color:var(--teal);white-space:nowrap}
.links{display:grid;grid-auto-flow:column;grid-template-rows:repeat(3,17px);font-size:10px;color:var(--muted);margin-top:12px}
.social{display:flex;gap:8px;margin-top:14px}
.social span{font-size:10px;color:#fff;background:#3b6fa8;height:18px;line-height:18px;padding:0 5px;border-radius:2px}
.social span.murmel{background:#2fa9df}
.social span.feed{background:#f08a24}
.bottom-bar{left:0;top:1150px;width:1002px;height:50px;background:linear-gradient(var(--teal-light),var(--teal))}
.copyright{left:82px;top:1167px;color:#fff;font-size:10px}
.cards{left:808px;top:1164px;display:flex;gap:6px}
.cards span{background:#fff;font-size:6.5px;color:#333;width:34px;height:18px;line-height:18px;text-align:center;border-radius:2px;white-space:nowrap}
</style>
</head>
<body>
<div class="abs top-rule"></div>
<div class="abs account-tab"><span>Register</span><span>|</span><span>Sign In</span></div>

<div class="abs brand"><div class="brand-dot"></div><div class="brand-name">Quay Server<br>Lantern</div></div>

<nav class="abs main-nav">
  <a href="#">Home</a><a href="#">Hosting</a><a href="#">Servers</a><a href="#">Hosting</a><a href="#">Domains</a><a href="#">Blog</a><a href="#">Get in Touch</a>
</nav>

<section class="abs hero"></section>
<div class="abs hero-kicker">Super-fast</div>
<div class="abs hero-title">Webhosting</div>
<div class="abs hero-sub">Great Value Solutions For Individuals, Small Businesses And Large Enterprises.</div>
<div class="abs hero-dots"><span></span><span></span><span></span></div>
<div class="abs hero-art" role="img" aria-label="Row of black server rack cabinets in perspective"></div>

<div class="abs feature-band"></div>
<div class="abs card" style="left:103px">
  <div class="card-head">Hosting<div class="card-icon" role="img" aria-label="Globe icon"></div></div>
  <p>Neque porro quisquam est, qui dolorem ipsum quia dolor sit amet,</p>
  <a class="btn" href="#">Read More</a>
</div>
<div class="abs card" style="left:377px">
  <div class="card-head">Domain Names<div class="card-icon drive" role="img" aria-label="Network drive with globe icon"></div></div>
  <div class="search"><svg width="14" height="14" viewBox="0 0 14 14" style="position:absolute;left:10px;top:10px"><circle cx="6" cy="6" r="4" fill="none" stroke="#888" stroke-width="1.6"/><line x1="9" y1="9" x2="12.5" y2="12.5" stroke="#888" stroke-width="1.8"/></svg></div>
  <a class="btn" href="#">Find Now</a>
</div>
<div class="abs card" style="left:649px">
  <div class="card-head">Servers<div class="card-icon tower" role="img" aria-label="Server tower icon"></div></div>
  <p>Neque porro quisquam est, qui dolorem ipsum quia dolor sit amet,</p>
  <a class="btn" href="#">Read More</a>
</div>

<section class="abs welcome"><h2>Welcome to <span>Quayserverlantern</span></h2></section>
<div class="abs video-frame"><div class="video-still" role="img" aria-label="Video still of a data centre server room"><div class="play"></div></div></div>
<div class="abs welcome-copy">
  <p>Nemo enim ipsam voluptatem quia voluptas sit aspernatur aut odit aut fugit, sed quia consequuntur magni dolores eos qui ratione voluptatem sequi nesciunt.</p>
  <p>Neque porro quisquam est, qui dolorem ipsum quia dolor sit amet, consectetur, adipisci velit, sed quia non numquam eius modi tempora incidunt ut labore et dolore magnam aliquam quaerat voluptatem.</p>
</div>
<a class="abs btn welcome-btn" href="#">Read More</a>

<aside class="abs testimonials">
  <h3>Testimonials <small>&lsaquo;&rsaquo;</small></h3>
  <div class="quote">
    <span class="quote-mark">&ldquo;</span>
    <p>Neque porro quisquam est, qui dolorem ipsum quia dolor sit amet, consectetur,</p>
    <p>adipisci velit, sed quia non numquam eius modi tempora incidunt ut labore et dolore magnam aliquam quaerat volup-tatem.</p>
  </div>
  <div class="stars">★★★★☆</div>
  <div class="author">- John Doe-</div>
</aside>

<div class="abs footer-col" style="left:81px;top:1024px">
  <h4>Products &amp; Services</h4>
  <div class="links" style="grid-template-columns:200px 150px">
    <span>Domain Registration and Transfer</span><span>DeckPanel Shared Hosting</span><span>DeckPanel ResellDesk Hosting</span>
    <span>Small Business Back-up</span><span>SSL Security Certificates</span><span>Cloud Virtual Servers</span>
  </div>
</div>
<div class="abs footer-col" style="left:454px;top:1024px">
  <h4>Intract with Us</h4>
  <div class="links" style="grid-template-columns:143px 100px">
    <span>Customer Helpdesk</span><span>Knowledgebase</span><span>Video Tutorials</span>
    <span>Live Chat</span><span>Network Status</span><span>Get In Touch</span>
  </div>
</div>
<div class="abs footer-col" style="left:744px;top:1024px">
  <h4>Connect with Us</h4>
  <div class="social"><span>Chatterleaf</span><span class="murmel">Murmel</span><span class="feed">Feed</span></div>
</div>

<footer class="abs bottom-bar"></footer>
<div class="abs copyright">Copyright © Quayserverlantern.com &nbsp;- All Rights Reserved</div>
<div class="abs cards"><span>Paywise</span><span>Cardloom</span><span>Roamcard</span></div>
</body>
</html>
```